Real Estate Business card design

Company Name: Tamarind Holdings, LLC
subtitle: We pay cash for houses!
Daniel Whitcombe
Managing Director
555-214-0963
Dan@TamarindHoldingsLLC.example
www.TamarindHoldingsLLC.example

We pay referral fees for Seller and Buyer leads.

Back:
We offer referral fees for Seller and Buyer leads that close.

Please contact Hal at 555-214-0963 with your referrals or to learn more about the referral program!

I am open to different color options but I am going for a classic, elegant, clean, and professional look. Please use logo as a reference.

Target Market(s)

People selling their homes and people in the market for buying homes.

Contact Information for Business Card

please see project description

Font styles to use
Serif
Sans Serif
Script

Requirements
Must have
• must have my logo in it
Nice to have
• I like cards that are split down the middle but please come up with a few mock ups. Open to any color scheme.

```html
<!DOCTYPE html>
<html lang="en">
<head>
<meta charset="utf-8">
<title>Tamarind Holdings, LLC — Business Card</title>
<link rel="stylesheet" href="https://fonts.googleapis.com/css2?family=Lato:ital,wght@0,400;0,700;1,400&display=swap">
<style>
  :root {
    --backdrop: #e4e5e6;
    --card-light: #f4f4f2;
    --card-dark: #474e59;
    --slate: #444b56;
    --gold: #c8a276;
    --light-text: #eef0f2;
    --divider: #e2d3bf;
  }
  * { margin: 0; padding: 0; box-sizing: border-box; }
  html, body {
    width: 1200px; height: 900px; overflow: hidden;
    background: var(--backdrop);
    font-family: "Lato", sans-serif;
  }
  .canvas { position: relative; width: 1200px; height: 900px; }
  .card {
    position: absolute; left: 349px; width: 509px; height: 290px;
    box-shadow: 0 3px 10px rgba(0,0,0,0.12);
  }
  .card--front { top: 122px; background: var(--card-light); }
  .card--back { top: 478px; background: var(--card-dark); }

  .brand {
    position: absolute; left: 34px; top: 96px; width: 170px;
    text-align: center;
  }
  .brand__name {
    font-size: 25px; font-weight: 700; line-height: 1.05;
    color: var(--slate);
  }
  .brand__tagline {
    margin-top: 10px; font-size: 12.5px; font-style: italic;
    color: var(--slate);
  }
  .divider {
    position: absolute; left: 238px; top: 66px; width: 1px; height: 184px;
    background: var(--divider);
  }
  .contact { position: absolute; left: 262px; top: 74px; color: var(--slate); }
  .contact__name { font-size: 17px; color: var(--gold); letter-spacing: 0.3px; }
  .contact__phone { margin-top: 6px; font-size: 13.5px; font-weight: 700; letter-spacing: 0.5px; }
  .contact__web { margin-top: 24px; font-size: 12px; line-height: 20px; }
  .contact__note { margin-top: 24px; font-size: 11.5px; font-style: italic; line-height: 15px; width: 200px; }

  .back-brand {
    position: absolute; right: 54px; top: 62px; width: 150px;
    text-align: right; font-size: 19px; font-weight: 700; line-height: 1.1;
    color: var(--light-text);
  }
  .back-copy {
    position: absolute; right: 54px; top: 190px;
    text-align: right; font-size: 12px; line-height: 17px; color: var(--light-text);
  }
  .back-copy__offer { font-style: italic; margin-bottom: 11px; }
  .accent { color: var(--gold); }
</style>
</head>
<body>
<main class="canvas">
  <section class="card card--front" aria-label="Card front">
    <div class="brand">
      <div class="brand__name">Tamarind Holdings, LLC</div>
      <div class="brand__tagline">We pay cash for houses!</div>
    </div>
    <div class="divider"></div>
    <div class="contact">
      <div class="contact__name">Daniel Whitcombe</div>
      <div class="contact__phone">555-214-0963</div>
      <div class="contact__web">
        Dan@TamarindHoldingsLLC.example<br>
        www.TamarindHoldingsLLC.example
      </div>
      <div class="contact__note">We pay referral fees for Seller and Buyer leads.</div>
    </div>
  </section>

  <section class="card card--back" aria-label="Card back">
    <div class="back-brand">Tamarind Holdings, LLC</div>
    <div class="back-copy">
      <p class="back-copy__offer">We offer referral fees for Seller and Buyer leads that close.</p>
      <p>Please contact <span class="accent">Hal</span> at <span class="accent">555-214-0963</span> with your referrals<br>or to learn more about the referral program!</p>
    </div>
  </section>
</main>
</body>
</html>
```